KELPMARROW, LLC needs a hybrid app to evaluate and develop athletes

KELPMARROW, LLC needs initial hybrid mobile app and website holding page. KELPMARROW, LLC allows athletes to develop their skills (soccer is initial sport) for free. Receive daily/weekly reminders. Access training videos. Earn points to "upgrade" their soccer profile in "app soccer store". See their points/rankings compared to all app users. Progress streak. This free app (for athletes) will communicate to paid app (coaches) in the future. We would like to see designs use the color blue. The design will communicate health and wellness.

```html
<!DOCTYPE html>
<html lang="en">
<head>
<meta charset="UTF-8">
<title>KELPMARROW – Athlete Login</title>
<link href="https://fonts.googleapis.com/css2?family=Montserrat:wght@500;600;800&display=swap" rel="stylesheet">
<style>
  :root {
    --page-bg: #ffffff;
    --blue-deep: #03529f;
    --blue-mid: #2a6db1;
    --blue-light: #5b8dc3;
    --button-bg: #0453a0;
    --button-edge: #0a3a6e;
    --field-line: rgba(255, 255, 255, 0.75);
    --text-light: #ffffff;
  }
  * { box-sizing: border-box; margin: 0; padding: 0; }
  html, body {
    width: 801px;
    height: 1200px;
    overflow: hidden;
    background: var(--page-bg);
    font-family: 'Montserrat', sans-serif;
    color: var(--text-light);
  }
  .screen {
    position: absolute;
    left: 63px;
    top: 64px;
    width: 675px;
    height: 1071px;
    background: linear-gradient(155deg, var(--blue-deep) 0%, var(--blue-mid) 50%, var(--blue-light) 100%);
    box-shadow: 0 0 8px rgba(0, 0, 0, 0.25);
  }
  .brand {
    position: absolute;
    top: 178px;
    width: 100%;
    text-align: center;
    font-weight: 800;
    font-size: 38px;
    letter-spacing: -0.5px;
  }
  .screen-title {
    position: absolute;
    top: 332px;
    width: 100%;
    text-align: center;
    font-weight: 500;
    font-size: 30px;
  }
  .login-form {
    position: absolute;
    left: 87px;
    top: 416px;
    width: 502px;
  }
  .field {
    display: flex;
    align-items: center;
    height: 88px;
    padding-left: 36px;
    border: 1.5px solid var(--field-line);
    font-weight: 500;
    font-size: 21px;
    margin-bottom: 26px;
  }
  .login-button {
    display: flex;
    align-items: center;
    justify-content: center;
    gap: 14px;
    height: 88px;
    margin-top: 5px;
    background: var(--button-bg);
    border-bottom: 5px solid var(--button-edge);
    border-radius: 2px;
    font-weight: 500;
    font-size: 21px;
    letter-spacing: 0.3px;
  }
  .login-button svg { width: 34px; height: 34px; }
  .create-account {
    position: absolute;
    top: 856px;
    width: 100%;
    text-align: center;
    font-weight: 500;
    font-size: 22px;
  }
  .create-account span {
    border-bottom: 1.5px solid var(--text-light);
    padding-bottom: 1px;
  }
</style>
</head>
<body>
  <main class="screen">
    <div class="brand">KELPMARROW</div>
    <h1 class="screen-title">Athlete Login</h1>
    <div class="login-form">
      <div class="field">Username</div>
      <div class="field">Password</div>
      <div class="login-button">
        <span>LOGIN</span>
        <svg viewBox="0 0 34 34" fill="none" stroke="#ffffff" stroke-width="1.6" stroke-linejoin="round" stroke-linecap="round" aria-hidden="true">
          <path d="M15 5 L29 2 L29 32 L15 29 Z"/>
          <path d="M15 5 L15 2 L20 2"/>
          <path d="M2 14 L13 14"/>
          <path d="M9 10 L13 14 L9 18"/>
        </svg>
      </div>
    </div>
    <div class="create-account"><span>CREATE ACCOUNT</span></div>
  </main>
</body>
</html>
```